Magician | Speaker looks for an innovative business card design

I'm a magician and public speaker offering artistic and modern magical experiences.
I'm based in Brussels (Belgium.) I love magic performed up-close, creating a space of intimacy, even when I'm on stage.
The final design should communicate professionalism, elegance, artistry, and a friendly kind personality

I would like to see designs based either on my photos and/or the way I sign my name Remy Vok (see attached files for more info.)
Additional photos and more info about what I offer can be seen at www.remy-vok.net

My current business card design is also attached. I like the fact that the reverse of my current design includes quotes from master magicians about magic, changing the way my participants see the art of magic.

Note: I would like a double-sided card design. However, I need white space on the reverse to be able to write things on for my performances.

Details to include on the card:
Artist name: Remy Vok
Offer: magician + (public) speaker or magic + (public) speaking (the + sign can be replaced by another character, like a bullet or a pipe)
Phone: +32 471 265 903
Email: book@remy-vok.net
(optional) Website: www.remy-vok.net or remy-vok.net

Target Market(s)

Corporate, organisations, companies as well as individuals

Industry/Entity Type

Artists

Colors

Designer to choose colors to be used in the design.

Requirements
Nice to have
• A side with a mirror could be nice

```html
<!DOCTYPE html>
<html lang="en">
<head>
<meta charset="utf-8">
<title>Remy Vok – Business Card</title>
<link rel="stylesheet" href="https://fonts.googleapis.com/css2?family=Open+Sans:wght@400;600&display=swap">
<style>
  :root {
    --page-bg: #e9e6e1;
    --card-white: #f4f4f4;
    --navy: #243f55;
    --accent-red: #b2391f;
    --ink-navy: #1f3a4f;
    --tag-grey: #6b6f73;
    --contact-white: #ffffff;
    --photo-dark: #1e1f26;
  }
  * { box-sizing: border-box; margin: 0; padding: 0; }
  html, body {
    width: 1200px;
    height: 900px;
    overflow: hidden;
    background: var(--page-bg);
    font-family: "Open Sans", Arial, sans-serif;
  }
  .card-sheet {
    position: absolute;
    inset: 0;
    display: flex;
    align-items: center;
    justify-content: center;
    gap: 40px;
  }
  .card {
    position: relative;
    width: 540px;
    height: 350px;
    overflow: hidden;
    box-shadow: 0 6px 18px rgba(0,0,0,0.18);
  }

  /* Front: two photographs side by side */
  .card-front { display: flex; background: var(--photo-dark); }
  .photo { flex: 1; height: 100%; }
  .photo-laughing {
    background: linear-gradient(135deg, #5a3427 0%, #3a2a28 45%, #22232c 100%);
  }
  .photo-cards {
    background: linear-gradient(160deg, #6a3f2e 0%, #3b2a27 40%, #1c1d24 100%);
  }

  /* Back: white field with navy wave */
  .card-back { background: var(--card-white); }
  .wave { position: absolute; inset: 0; width: 100%; height: 100%; }
  .wave-navy { fill: var(--navy); }
  .wave-accent { fill: none; stroke: var(--accent-red); stroke-width: 5; }

  .brand {
    position: absolute;
    right: 40px;
    top: 40px;
    text-align: right;
  }
  .brand-name {
    font-size: 40px;
    font-weight: 400;
    color: var(--ink-navy);
    letter-spacing: 1px;
    line-height: 1;
  }
  .brand-tagline {
    margin-top: 14px;
    font-size: 12px;
    font-weight: 400;
    letter-spacing: 2px;
    color: var(--tag-grey);
    text-transform: uppercase;
  }
  .website {
    position: absolute;
    right: 34px;
    top: 196px;
    color: var(--contact-white);
    font-size: 15px;
    letter-spacing: 0.5px;
  }
  .contact {
    position: absolute;
    left: 44px;
    bottom: 38px;
    color: var(--contact-white);
    font-size: 19px;
    line-height: 1.45;
  }
</style>
</head>
<body>
  <main class="card-sheet">
    <section class="card card-front" aria-label="Card front">
      <div class="photo photo-laughing" role="img" aria-label="Photo of the magician laughing among soap bubbles in front of a brick wall"></div>
      <div class="photo photo-cards" role="img" aria-label="Photo of the magician smiling while handling a deck of playing cards"></div>
    </section>

    <section class="card card-back" aria-label="Card back">
      <svg class="wave" viewBox="0 0 540 350" preserveAspectRatio="none" aria-hidden="true">
        <path class="wave-accent" d="M0,218 C120,186 260,200 360,186 C450,173 510,152 540,134"/>
        <path class="wave-navy" d="M0,234 C120,202 260,216 365,201 C455,188 512,167 540,150 L540,350 L0,350 Z"/>
      </svg>

      <div class="brand">
        <div class="brand-name">Remy Vok</div>
        <div class="brand-tagline">Magician &amp; Public Speaker</div>
      </div>

      <div class="website">www.remy-vok.net</div>

      <div class="contact">
        <div class="contact-phone">+32 471 265 903</div>
        <div class="contact-email">book@remy-vok.net</div>
      </div>
    </section>
  </main>
</body>
</html>
```